Book Cover for my Autobiography

I would like to see a CONCEPT of the Front Cover as per the following.
a) Take me out of the FILE NAMED=1-MAIN.jpg
b) I want my Wife "Watching over me" - behind me - in the SHADOWS. You can take her image for the concept from the FILE NAMED=2-Wife Watching over me.jpg.
c) This based on the old saying that "Behind every Good Man....is a Woman".  So that's what I want to convert because my wife has always been in the background, in the "Shadows" - always supporting and encouraging me in whatever I do.
d) This book is purely for my children, wife, siblings, relatives and Friends.
e) the Book Cover has to be designed FLAT & RECTANGULAR - like the sample leather cover.  i.e. NOT viewed from an Angle.
f) The Book Title is "Salt in the Orchard"
g) I have no pre-conceived ideas of design or colours or styling etc.  I want a PROFESSIONAL DESIGNER to come up with the best Overall Design that conveys the "Supportive Wife" always behind me and supporting me - While I am out front as the subject.
h) When the Design is accepted, I will provide the main photo of my wife without my son in front of her that I want to use - and one me without my wife's arms around me.  But if you can do that too (i.e. reconstruct my Wife's Burgundy top & and remove her arms from around me-then even better because I don't have to hire another graphic designer to do that for me).
My name is "Tomas Brenhoek" so the author of the autobiography needs to be SOMEWHERE.
h) And last, please just put some text - maybe 2 sentences for the summary of the story like many Autobiographies do. eg.
"My story of how ....Lorem ipsum dolor sit amet, consectetur adipiscing elit, sed do eiusmod tempor incididunt. Integer vitae justo eget magna fermentum iaculis eu non. Aliquam eleifend".

I forgot to mention that this Book Cover is actually going on an eBOOK - not a Printed Book.
It's just for Family and Friends.

```html
<!DOCTYPE html>
<html lang="en">
<head>
<meta charset="utf-8">
<title>Salt in the Orchard — Tomas Brenhoek</title>
<link href="https://fonts.googleapis.com/css2?family=Bebas+Neue&family=Allison&family=Catamaran:wght@300;400&family=Playfair+Display:wght@700&display=swap" rel="stylesheet">
<style>
  :root{
    --navy:#0a3f68;
    --navy-deep:#08355a;
    --white:#ffffff;
    --script-red:#c0232b;
    --quote-red:#8f2b24;
    --wife-top:#8c2a22;
    --hair:#1b1a1c;
    --skin:#c79a82;
    --jacket:#13345a;
  }
  *{margin:0;padding:0;box-sizing:border-box}
  html,body{width:849px;height:1200px;overflow:hidden;background:var(--navy)}
  .cover{position:relative;width:849px;height:1200px;overflow:hidden;
    background:linear-gradient(180deg,var(--navy) 0%,var(--navy-deep) 100%)}
  .title-main{position:absolute;left:0;top:40px;width:849px;text-align:center;
    font-family:"Bebas Neue",Impact,sans-serif;color:var(--white);
    font-size:205px;line-height:1;letter-spacing:1px;white-space:nowrap}
  .photo{position:absolute}
  .photo-wife{left:95px;top:185px;width:450px;height:740px}
  .photo-author{left:215px;top:330px;width:634px;height:870px}
  .title-script{position:absolute;left:440px;top:115px;
    font-family:"Allison",cursive;color:var(--script-red);
    font-size:190px;line-height:1;transform:rotate(-8deg);white-space:nowrap}
  .mark{position:absolute;font-family:"Playfair Display",Georgia,serif;
    color:var(--quote-red);font-size:190px;line-height:1}
  .mark-open{left:70px;top:815px}
  .mark-close{left:680px;top:970px}
  .blurb{position:absolute;left:130px;top:880px;width:590px;text-align:center;
    font-family:"Catamaran",sans-serif;font-weight:300;color:var(--white);
    font-size:25px;line-height:34px}
  .author{position:absolute;left:0;top:1105px;width:849px;text-align:center;
    font-family:"Catamaran",sans-serif;font-weight:400;color:var(--white);
    font-size:46px;letter-spacing:1px}
</style>
</head>
<body>
<main class="cover">
  <h1 class="title-main">SALT IN THE</h1>

  <svg class="photo photo-wife" viewBox="0 0 450 740" role="img" aria-label="Photograph of the author's wife in a burgundy top, standing behind him in soft shadow">
    <defs>
      <linearGradient id="wifeFade" x1="0" y1="0" x2="0" y2="1">
        <stop offset="0" stop-color="var(--hair)"/>
        <stop offset="0.45" stop-color="var(--skin)" stop-opacity="0.85"/>
        <stop offset="0.6" stop-color="var(--wife-top)"/>
        <stop offset="1" stop-color="var(--wife-top)" stop-opacity="0"/>
      </linearGradient>
    </defs>
    <path d="M160 10 C260 -10 360 40 380 150 C395 260 430 330 420 420 L450 440 L450 740 L10 740 L0 500 C0 440 30 400 60 380 C40 300 40 180 80 90 C100 40 130 20 160 10 Z" fill="url(#wifeFade)"/>
  </svg>

  <svg class="photo photo-author" viewBox="0 0 634 870" role="img" aria-label="Photograph of the author, smiling, in a navy jacket over a red checked shirt">
    <defs>
      <linearGradient id="authorFade" x1="0" y1="0" x2="0" y2="1">
        <stop offset="0" stop-color="var(--hair)"/>
        <stop offset="0.4" stop-color="var(--skin)"/>
        <stop offset="0.55" stop-color="var(--jacket)"/>
        <stop offset="1" stop-color="var(--jacket)"/>
      </linearGradient>
    </defs>
    <path d="M290 0 C420 -10 520 80 515 230 C512 320 500 380 470 420 C560 440 634 480 634 520 L634 870 L20 870 C10 720 60 620 180 560 C230 540 290 520 300 500 C250 450 225 360 230 260 C220 120 230 20 290 0 Z" fill="url(#authorFade)"/>
  </svg>

  <div class="title-script">Orchard</div>

  <span class="mark mark-open" aria-hidden="true">&ldquo;</span>
  <p class="blurb">My story of how ….Lorem ipsum dolor sit amet, consectetur adipiscing elit, sed do eiusmod tempor incididunt. Integer vitae justo eget magna fermentum iaculis eu non. Aliquam eleifend</p>
  <span class="mark mark-close" aria-hidden="true">&rdquo;</span>

  <p class="author">TOMAS BRENHOEK</p>
</main>
</body>
</html>
```